Flyer Design

Company name Glimbra, ecofriendly oven cleaning. See website glimbra-example.co.uk. Looking for a flyer to offer a 10% discount off web prices Picture of shiny oven, highlighting eco aspect

Industry/Entity Type

It Company

```html
<!DOCTYPE html>
<html lang="en">
<head>
<meta charset="utf-8">
<title>Glimbra – eco-friendly oven cleaning flyer</title>
<link rel="stylesheet" href="https://fonts.googleapis.com/css2?family=Source+Sans+3:wght@300;400;600;700&display=swap">
<style>
  :root {
    --green: #8dc63f;
    --green-dark: #3f9a3a;
    --badge: #3aa14a;
    --green-pale: #c5e0a8;
    --ink: #222222;
    --grey-text: #555555;
    --line-grey: #e4e6e8;
    --paper: #ffffff;
  }
  * { margin: 0; padding: 0; box-sizing: border-box; }
  html, body { width: 921px; height: 1200px; overflow: hidden; background: var(--paper); }
  body { font-family: "Source Sans 3", "Helvetica Neue", Arial, sans-serif; color: var(--ink); }
  .flyer { position: relative; width: 921px; height: 1200px; overflow: hidden; background: var(--paper); }
  .flyer-shapes { position: absolute; inset: 0; }

  .brand { position: absolute; left: 42px; top: 22px; }
  .brand-name { font-size: 84px; font-weight: 700; color: var(--green); line-height: 1; letter-spacing: -1px; }
  .brand-tagline { font-size: 25px; font-weight: 600; color: var(--green); opacity: .75; margin-top: 0; }

  .banner-text { position: absolute; left: 42px; top: 514px; color: #fff; font-weight: 300; font-size: 32px; line-height: 38px; }

  .badge { position: absolute; left: 597px; top: 476px; width: 166px; height: 166px; border-radius: 50%;
           background: var(--green-pale); display: flex; align-items: center; justify-content: center; }
  .badge-inner { width: 130px; height: 130px; border-radius: 50%; background: var(--badge); color: #fff;
                 display: flex; flex-direction: column; align-items: center; justify-content: center;
                 font-weight: 600; line-height: 1.15; }
  .badge-big { font-size: 28px; }
  .badge-big small { font-size: 21px; }
  .badge-small { font-size: 21px; }

  .intro { position: absolute; left: 40px; top: 658px; width: 460px; }
  .intro-headline { font-size: 28px; font-weight: 400; color: var(--green-dark); line-height: 33px; }
  .intro-lead { font-size: 22px; font-weight: 400; color: var(--ink); line-height: 27px; margin-top: 8px; }
  .intro-body { font-size: 17.5px; font-weight: 400; color: var(--grey-text); line-height: 22px; margin-top: 16px; text-align: justify; width: 440px; }
  .services-title { font-size: 20px; margin-top: 18px; }
  .services { list-style: none; display: grid; grid-template-columns: 165px 165px; row-gap: 4px; margin-top: 8px; }
  .services li { display: flex; align-items: center; gap: 8px; font-size: 20px; line-height: 24px; }
  .services svg { width: 17px; height: 17px; flex: none; }

  .oven-photo { position: absolute; left: 529px; top: 709px; width: 350px; height: 318px;
                background: linear-gradient(180deg, #c9cccf 0%, #b5b9bc 12%, #2a2b2d 22%, #4b4d50 55%, #1c1d1f 85%, #b8bbbe 100%); }
  .oven-inset { position: absolute; left: 693px; top: 914px; width: 202px; height: 202px; border-radius: 50%;
                background: var(--green-pale); display: flex; align-items: center; justify-content: center; }
  .oven-inset-photo { width: 178px; height: 178px; border-radius: 50%;
                      background: radial-gradient(circle at 45% 50%, #8e8c86 0%, #6e6a62 45%, #4a4640 100%); }

  .van-photo { position: absolute; left: 414px; top: 31px; width: 196px; height: 101px; border-radius: 30px 40px 14px 14px;
               background: linear-gradient(180deg, #f4f5f5 0%, #dfe2e3 70%, #3a3c3e 100%); }

  .contact { position: absolute; left: 0; right: 0; top: 1110px; text-align: center; color: #fff; }
  .contact-call { font-size: 29px; font-weight: 300; }
  .contact-web { font-size: 27px; font-weight: 700; letter-spacing: 1.5px; margin-top: 2px; }
</style>
</head>
<body>
<main class="flyer">
  <svg class="flyer-shapes" width="921" height="1200" viewBox="0 0 921 1200">
    <defs>
      <linearGradient id="kitchenTones" x1="0" y1="0" x2="1" y2="1">
        <stop offset="0" stop-color="#e9e7e2"/>
        <stop offset=".45" stop-color="#d6d1c8"/>
        <stop offset=".7" stop-color="#a89c8a"/>
        <stop offset="1" stop-color="#6f7a6a"/>
      </linearGradient>
    </defs>
    <rect class="kitchen-photo" role="img" aria-label="Photograph of a bright modern fitted kitchen with built-in oven" x="0" y="40" width="921" height="640" fill="url(#kitchenTones)"/>
    <path class="header-fill" d="M0,0 H921 V70 C650,175 300,250 0,200 Z" fill="var(--paper)"/>
    <path class="header-swoosh" d="M0,185 C300,235 640,150 921,0 L921,70 C650,185 300,262 0,218 Z" fill="var(--green-pale)"/>
    <path class="body-fill" d="M0,640 C250,600 600,620 921,700 V1200 H0 Z" fill="var(--paper)"/>
    <path class="body-edge" d="M560,625 C700,640 820,665 921,725 L921,700 C820,660 700,630 560,620 Z" fill="var(--line-grey)"/>
    <path class="banner-edge" d="M0,520 C170,482 420,490 640,560 C420,635 170,640 0,640 Z" fill="var(--green-pale)"/>
    <path class="banner-fill" d="M0,505 C170,468 420,476 630,548 C420,615 170,620 0,622 Z" fill="var(--green)"/>
    <path class="footer-edge" d="M0,1050 C300,1100 650,1110 921,1040 V1060 C650,1125 300,1118 0,1068 Z" fill="var(--line-grey)"/>
    <path class="footer-fill" d="M0,1062 C300,1112 650,1120 921,1052 V1200 H0 Z" fill="var(--green)"/>
  </svg>

  <div class="van-photo" role="img" aria-label="Photograph of the company's white service van"></div>

  <header class="brand">
    <div class="brand-name">glimbra</div>
    <div class="brand-tagline">eco-friendly oven cleaning</div>
  </header>

  <div class="banner-text">
    <div>Your local professional</div>
    <div>OVEN CLEANING COMPANY</div>
  </div>

  <div class="badge">
    <div class="badge-inner">
      <div class="badge-big">10% <small>OFF</small></div>
      <div class="badge-small">WEB PRICES</div>
    </div>
  </div>

  <section class="intro">
    <h1 class="intro-headline">Got an oven covered in dirt,<br>grease or grime?</h1>
    <p class="intro-lead">Hire the oven cleaning experts and<br>let us do a job you hate!</p>
    <p class="intro-body">100% environmentally friendly products in our oven cleaning process.<br>We clean ovens without the use of the pungent chemicals that are available to you in the super-market.</p>
    <p class="services-title">We specialise in cleaning:</p>
    <ul class="services">
      <li><svg viewBox="0 0 20 20"><circle cx="10" cy="10" r="8.5" fill="none" stroke="#3f9a3a" stroke-width="1.8"/><path d="M8,6 L12,10 L8,14" fill="none" stroke="#3f9a3a" stroke-width="1.8"/></svg>Ovens</li>
      <li><svg viewBox="0 0 20 20"><circle cx="10" cy="10" r="8.5" fill="none" stroke="#3f9a3a" stroke-width="1.8"/><path d="M8,6 L12,10 L8,14" fill="none" stroke="#3f9a3a" stroke-width="1.8"/></svg>Ranges</li>
      <li><svg viewBox="0 0 20 20"><circle cx="10" cy="10" r="8.5" fill="none" stroke="#3f9a3a" stroke-width="1.8"/><path d="M8,6 L12,10 L8,14" fill="none" stroke="#3f9a3a" stroke-width="1.8"/></svg>Hobs</li>
      <li><svg viewBox="0 0 20 20"><circle cx="10" cy="10" r="8.5" fill="none" stroke="#3f9a3a" stroke-width="1.8"/><path d="M8,6 L12,10 L8,14" fill="none" stroke="#3f9a3a" stroke-width="1.8"/></svg>Cookers</li>
      <li><svg viewBox="0 0 20 20"><circle cx="10" cy="10" r="8.5" fill="none" stroke="#3f9a3a" stroke-width="1.8"/><path d="M8,6 L12,10 L8,14" fill="none" stroke="#3f9a3a" stroke-width="1.8"/></svg>Extractors</li>
      <li><svg viewBox="0 0 20 20"><circle cx="10" cy="10" r="8.5" fill="none" stroke="#3f9a3a" stroke-width="1.8"/><path d="M8,6 L12,10 L8,14" fill="none" stroke="#3f9a3a" stroke-width="1.8"/></svg>Barbecues</li>
    </ul>
  </section>

  <div class="oven-photo" role="img" aria-label="Photograph of a shiny clean stainless steel built-in oven"></div>
  <div class="oven-inset">
    <div class="oven-inset-photo" role="img" aria-label="Close-up photograph of an oven interior, half dirty and half cleaned"></div>
  </div>

  <footer class="contact">
    <div class="contact-call">To Book Call Us Now 07700 900123</div>
    <div class="contact-web">www.glimbra-example.co.uk</div>
  </footer>
</main>
</body>
</html>
```